Web app UI design

This web app has been built and the UI needs a refresh.

Attached are the pages which need the refresh.

The web app is for a cyber security product/service and customers are inputting their details.

```html
<!DOCTYPE html>
<html lang="en">
<head>
<meta charset="utf-8">
<title>Verify</title>
<link href="https://fonts.googleapis.com/css2?family=Inter:wght@400;500;600;700&display=swap" rel="stylesheet">
<style>
  :root {
    --bg: #1c1f29;
    --sidebar-line: #262a35;
    --card: #20242f;
    --field: #252a35;
    --divider: #2f3441;
    --text: #ffffff;
    --text-muted: #a7abb5;
    --text-faint: #4a505d;
    --icon: #6c717d;
    --accent: #2a63e6;
    --online: #22d35e;
  }
  * { box-sizing: border-box; margin: 0; padding: 0; }
  html, body { width: 1200px; height: 716px; overflow: hidden; background: var(--bg); }
  body { font-family: "Inter", sans-serif; color: var(--text); position: relative; }

  .app { position: absolute; inset: 0; background: var(--bg); border-radius: 20px; overflow: hidden; }

  .sidebar { position: absolute; left: 0; top: 0; width: 101px; height: 716px; border-right: 1px solid var(--sidebar-line); }
  .menu-toggle { position: absolute; left: 37px; top: 38px; width: 30px; height: 12px; }
  .nav-icon { position: absolute; left: 35px; width: 34px; height: 34px; }
  .nav-icon.active-wrap { left: 25px; width: 53px; height: 53px; top: 324px; background: var(--accent); border-radius: 8px; display: flex; align-items: center; justify-content: center; }
  .avatar { position: absolute; left: 35px; top: 635px; width: 34px; height: 34px; border-radius: 50%; background: radial-gradient(circle at 50% 40%, #8a6a58, #3d3530); }
  .avatar-status { position: absolute; left: 64px; top: 641px; width: 9px; height: 9px; border-radius: 50%; background: var(--online); }

  .page-title { position: absolute; left: 145px; top: 31px; font-size: 16px; font-weight: 400; color: var(--text-muted); }

  .verify-card { position: absolute; left: 184px; top: 101px; width: 936px; height: 506px; background: var(--card); border-radius: 20px; }

  .info-panel { position: absolute; left: 229px; top: 147px; width: 335px; height: 413px; border-radius: 20px; overflow: hidden;
    background: linear-gradient(180deg, #2c66ea 0%, #2a62e8 50%, #1d4fd0 80%, #1643b8 100%); }
  .info-panel p { position: absolute; left: 32px; top: 28px; width: 280px; font-size: 25px; line-height: 29px; font-weight: 500; }
  .info-art { position: absolute; left: 0; top: 220px; width: 335px; height: 193px;
    background: radial-gradient(ellipse at 65% 60%, rgba(140,185,255,0.55), rgba(40,95,225,0) 60%); }

  .form { position: absolute; left: 634px; top: 0; }
  .form-title { position: absolute; left: 634px; top: 146px; font-size: 33px; font-weight: 700; letter-spacing: -0.3px; white-space: nowrap; }
  .label { position: absolute; font-size: 13px; font-weight: 400; white-space: nowrap; }
  .label.faint { font-size: 11.5px; color: var(--text-faint); }
  .value { position: absolute; font-size: 13.5px; white-space: nowrap; }
  .value.faint { color: var(--text-faint); }
  .divider { position: absolute; left: 623px; top: 265px; width: 441px; height: 1px; background: var(--divider); }
  .field { position: absolute; top: 323px; width: 207px; height: 46px; background: var(--field); border-radius: 12px; font-size: 13.5px; padding-left: 17px; line-height: 46px; }
  .hidden-label { position: absolute; left: 634px; top: 401px; font-size: 16px; }
  .checkbox { position: absolute; left: 634px; top: 436px; width: 23px; height: 23px; border: 1.5px solid var(--accent); border-radius: 4px; display: flex; align-items: center; justify-content: center; }
  .save-button { position: absolute; left: 634px; top: 508px; width: 207px; height: 46px; background: var(--accent); border-radius: 12px; border: none; color: var(--text); font-family: "Inter", sans-serif; font-size: 13.5px; font-weight: 600; }
</style>
</head>
<body>
<div class="app">
  <aside class="sidebar">
    <svg class="menu-toggle" viewBox="0 0 30 12" fill="none" stroke="#fff" stroke-width="1.6" stroke-linecap="round"><line x1="1" y1="2" x2="29" y2="2"/><line x1="1" y1="10" x2="14" y2="10"/></svg>
    <svg class="nav-icon" style="top:100px" viewBox="0 0 24 24" fill="none" stroke="var(--icon)" stroke-width="1.4" stroke-linejoin="round"><path d="M3 10.5 12 3l9 7.5V21h-6v-6H9v6H3z"/></svg>
    <svg class="nav-icon" style="top:177px" viewBox="0 0 24 24" fill="none" stroke="var(--icon)" stroke-width="1.4" stroke-linecap="round"><circle cx="11" cy="7" r="4"/><path d="M3 21c0-4 3-7 8-7 1.5 0 2.8.3 3.8.8"/><path d="M15 21l1-3 4-4 2 2-4 4z"/></svg>
    <svg class="nav-icon" style="top:255px" viewBox="0 0 24 24" fill="none" stroke="var(--icon)" stroke-width="1.4" stroke-linecap="round" stroke-linejoin="round"><rect x="5" y="2" width="12" height="20" rx="3"/><path d="M10 17v-8a1.2 1.2 0 0 1 2.4 0v4m0-1a1.2 1.2 0 0 1 2.4 0v1m0 0a1.2 1.2 0 0 1 2.4 0v1a1.2 1.2 0 0 1 2.4 0v2c0 2-1 4-3 4"/></svg>
    <div class="nav-icon active-wrap">
      <svg width="30" height="30" viewBox="0 0 24 24" fill="none" stroke="#fff" stroke-width="1.5" stroke-linecap="round" stroke-linejoin="round"><circle cx="11" cy="7" r="4"/><path d="M3 21c0-4 3-7 8-7 1.2 0 2.3.2 3.2.5"/><path d="M14 19l2.5 2.5L22 16"/></svg>
    </div>
    <div class="avatar" role="img" aria-label="User profile photo"></div>
    <div class="avatar-status"></div>
  </aside>

  <h1 class="page-title">Verify</h1>

  <section class="verify-card"></section>

  <div class="info-panel">
    <p>This info will be shown on your profile page</p>
    <div class="info-art" role="img" aria-label="Illustration of an open padlock with floating spheres and circuit lines"></div>
  </div>

  <h2 class="form-title">Verify Info</h2>
  <span class="label faint" style="left:634px;top:202px">Company Legal Name</span>
  <span class="value" style="left:634px;top:224px">Company name</span>
  <span class="label" style="left:866px;top:206px">ACN</span>
  <span class="value faint" style="left:866px;top:224px">6688886698</span>
  <span class="label" style="left:990px;top:206px">ABN</span>
  <span class="value faint" style="left:990px;top:224px">5474898983</span>
  <div class="divider"></div>

  <span class="label" style="left:634px;top:297px">BSB</span>
  <div class="field" style="left:634px">099999</div>
  <span class="label" style="left:866px;top:297px">Account</span>
  <div class="field" style="left:866px">2245555</div>

  <span class="hidden-label">Hidden</span>
  <div class="checkbox">
    <svg width="15" height="15" viewBox="0 0 16 16" fill="none" stroke="#fff" stroke-width="1.6" stroke-linecap="round" stroke-linejoin="round"><path d="M2 8.5l4 4L14 4"/></svg>
  </div>

  <button class="save-button">Save verify data</button>
</div>
</body>
</html>
```